Skyforge Technics Inc. - new Website

1 - Take the existing content and elevate the site to be much more dynamic. www.skyforgenorth.example. We are looking for a site that is modern and easily updated. Aerospace is our primary industry but rail and engineering are part of who we are.

2- New logo to implement (attached)

3 - Remove customer access page

4 - website to be built so that we can change and update from our offices with no coding requirements.

5 - Pictures available

6 - Bilingual French and English

7 - News / Press page

8 - Social media icons link Twitter, youtube and linkedin

9 - add an PLUME engineering page (content will be added later) Plume logo attached

10 - Please use stock photos, and but will pay for royalty if necessary

Target Market(s)

Airlines 80%
Rail 10%
Other transportation 10%

Industry/Entity Type

Aviation

Number of Pages Required

5+ page

Font styles to use
Sans Serif

Requirements
Must have
• Skyforge logo
• Logo Plume (Skyforge Validation Bureau Partners inc.)
• Dynamic modern look and feel
• Existing content from our website and attched introduction document plus the above
• Press page
• Industry pictures - Repair (as per our website)
Nice to have
• Animation
• You tube links
• Blog
• Career page

```html
<!DOCTYPE html>
<html lang="en">
<head>
<meta charset="utf-8">
<title>Skyforge Technics Inc.</title>
<link href="https://fonts.googleapis.com/css2?family=Open+Sans:wght@400;600;700&family=Roboto+Condensed:wght@400;700&display=swap" rel="stylesheet">
<style>
:root{
  --brand:#1f5fa6;
  --brand-dark:#17497f;
  --nav:#2a6db3;
  --accent:#d0262f;
  --ink:#333a42;
  --muted:#6b7480;
  --soft:#eef1f4;
  --footer:#10294a;
  --footer-low:#0a1d36;
  --white:#fff;
}
*{box-sizing:border-box;margin:0;padding:0}
html,body{width:1200px;height:2504px;overflow:hidden;background:var(--white)}
body{font-family:"Open Sans",Arial,sans-serif;color:var(--ink);position:relative}
.section{position:absolute;left:0;width:1200px}
.title{font-family:"Roboto Condensed",Arial,sans-serif;font-weight:700;color:var(--brand);text-align:center;letter-spacing:1px}
.btn{display:inline-block;background:var(--brand);color:var(--white);font-size:11px;font-weight:700;padding:8px 16px;text-transform:uppercase;letter-spacing:.5px}
.btn-red{background:var(--accent)}
.photo{display:block}

/* header */
.site-header{top:0;height:136px}
.brand{position:absolute;left:28px;top:20px;display:flex;align-items:center;gap:12px}
.brand-mark{width:64px;height:64px;background:var(--brand)}
.brand-name{font-size:16px;font-weight:700;color:var(--brand);line-height:1.3;width:170px}
.clocks{position:absolute;right:110px;top:44px;display:flex;gap:8px}
.clock{border:1px solid #b9c6d6;width:88px;height:40px;text-align:center;font-size:10px;color:var(--brand);padding-top:5px;line-height:1.4}
.clock b{display:block;color:var(--accent);font-size:11px}
.lang{position:absolute;right:28px;top:52px;border:1px solid #b9c6d6;font-size:10px;padding:4px 8px;color:var(--ink)}
.main-nav{top:136px;height:36px;background:var(--nav);display:flex;align-items:center;padding-left:28px}
.main-nav a{color:var(--white);font-size:11px;font-weight:600;text-transform:uppercase;padding:0 14px;line-height:36px;text-decoration:none}
.main-nav a.active{background:var(--brand-dark)}

/* hero */
.hero{top:172px;height:468px;background:linear-gradient(135deg,#3e5a73 0%,#7f95a8 40%,#566a7c 70%,#c7a13a 100%)}
.hero-badge{position:absolute;left:450px;top:120px;width:300px;height:130px;background:rgba(255,255,255,.9);display:flex;align-items:center;justify-content:center;gap:12px}
.hero-badge .brand-mark{width:48px;height:48px}
.hero-badge .brand-name{width:auto;font-size:15px}
.hero .btn{position:absolute;left:546px;top:268px}
.hero-arrow{position:absolute;top:220px}

/* welcome */
.welcome{top:640px;height:430px}
.welcome .media{position:absolute;left:50px;top:66px;width:470px;height:290px;background:linear-gradient(160deg,#cfe0ee,#7fa6c9 55%,#dfe6ea)}
.welcome .play{position:absolute;left:60px;top:118px}
.welcome h1{position:absolute;left:560px;top:86px;font-family:"Roboto Condensed",Arial,sans-serif;font-size:30px;color:var(--brand);font-weight:700;text-transform:uppercase}
.welcome p{position:absolute;left:560px;top:136px;width:580px;font-size:12px;line-height:1.75;color:var(--muted)}
.welcome .btn{position:absolute;left:560px;top:300px}

/* services */
.services{top:1070px;height:490px;background:linear-gradient(180deg,#e4e9ee,#f4f6f8)}
.services .title{position:absolute;top:40px;width:100%;font-size:32px}
.svc{position:absolute;top:108px;width:240px;text-align:center}
.svc .photo{width:240px;height:176px}
.svc h3{font-size:12px;font-weight:700;text-transform:uppercase;margin:14px 0 8px;color:var(--ink)}
.svc p{font-size:11px;line-height:1.6;color:var(--muted);padding:0 10px;height:54px}
.svc .btn{margin-top:12px}

/* products */
.products{top:1560px;height:400px}
.products .title{position:absolute;top:42px;width:100%;font-size:34px}
.prod{position:absolute;top:118px;width:230px;text-align:center}
.prod .photo{width:230px;height:184px}
.prod h4{font-size:12px;font-weight:700;text-transform:uppercase;margin-top:14px}
.prod span{font-size:11px;color:var(--brand);text-decoration:underline}

/* partners */
.partners{top:1960px;height:320px;background:var(--soft)}
.partners .title{position:absolute;top:50px;width:100%;font-size:30px}
.partner-row{position:absolute;top:140px;left:80px;width:1040px;display:flex;justify-content:space-between}
.partner{width:172px;height:84px;background:var(--white);display:flex;align-items:center;justify-content:center;font-weight:700;font-size:15px;color:var(--brand);text-align:center}
.p-arrow{position:absolute;top:170px}

/* footer */
.site-footer{top:2280px;height:200px;background:var(--footer);color:#c9d3df}
.fcol{position:absolute;top:26px}
.fcol h5{font-size:13px;font-weight:700;color:var(--white);text-transform:uppercase;margin-bottom:12px}
.fcol ul{list-style:none;font-size:11px;line-height:1.8}
.map{width:200px;height:100px;background:linear-gradient(135deg,#e7e2d3,#c9d9c0)}
.addr-line{display:flex;gap:8px;align-items:center;font-size:11px;margin-bottom:10px}
.newsletter p{font-size:11px;line-height:1.6;width:240px;margin-bottom:10px}
.field{width:220px;height:28px;background:var(--white);color:#999;font-size:11px;padding:6px 8px;margin-bottom:8px}
.social{position:absolute;right:40px;top:160px;display:flex;gap:8px}
.social i{width:22px;height:22px;background:#2c4d78;display:block}
.footer-bar{top:2480px;height:24px;background:var(--footer-low);color:#8ea0b6;font-size:10px;line-height:24px;padding:0 28px}
</style>
</head>
<body>

<header class="section site-header">
  <div class="brand"><span class="brand-mark"></span><span class="brand-name">Skyforge Technics Inc.</span></div>
  <div class="clocks">
    <div class="clock">Montreal (EST)<b>10:15</b></div>
    <div class="clock">Toronto (EST)<b>10:15</b></div>
    <div class="clock">Vancouver (PST)<b>07:15</b></div>
  </div>
  <div class="lang">English ▾</div>
</header>

<nav class="section main-nav">
  <a class="active">Home</a><a>Services</a><a>Plume Engineering</a><a>Locations</a><a>People</a><a>Quality</a><a>Sales Presentation</a><a>Partners</a><a>Contact Us</a><a>History</a>
</nav>

<section class="section hero" role="img" aria-label="Technicians repairing aircraft seat parts in the workshop">
  <div class="hero-badge"><span class="brand-mark"></span><span class="brand-name">Skyforge Technics Inc.</span></div>
  <span class="btn btn-red">Read more info</span>
  <svg class="hero-arrow" style="left:20px" width="24" height="40"><path d="M18 4 L6 20 L18 36" stroke="#fff" stroke-width="3" fill="none"/></svg>
  <svg class="hero-arrow" style="right:20px" width="24" height="40"><path d="M6 4 L18 20 L6 36" stroke="#fff" stroke-width="3" fill="none"/></svg>
</section>

<section class="section welcome">
  <div class="media" role="img" aria-label="Skyforge facility building exterior"></div>
  <svg class="play" style="left:240px;top:184px;position:absolute" width="60" height="42"><rect width="60" height="42" rx="10" fill="#d0262f"/><path d="M24 12 L40 21 L24 30Z" fill="#fff"/></svg>
  <h1>Welcome to Skyforge Service Inc</h1>
  <p>The Company's services extend from repair and maintenance of interior and cargo parts for commercial aircraft. Skyforge offers a dramatically lower cost outsourcing alternative to airlines for the maintenance, repair and management of the following non-flight critical commodities: cargo containers, galleys, coffee makers, ovens, carts, cabin interiors including video systems, audio systems and on-board telephone systems, passenger seats, and other cabin furnishings. The Company's main manufacturing division in Harbourview, Canada, performs cut and sew services for seat covers and trim cutting and sewing of carpets, serving airlines for over twenty years.</p>
  <span class="btn">View more info</span>
</section>

<section class="section services">
  <h2 class="title">OUR SERVICES</h2>
  <div class="svc" style="left:60px"><div class="photo" style="background:linear-gradient(150deg,#5b7fa0,#a7b9c8)" role="img" aria-label="Technician servicing cabin parts"></div><h3>Lav Cabin Maintenance</h3><p>The Company's service team focus is on fast turnaround of cabin equipment found in the interior and cargo.</p><span class="btn">Read more</span></div>
  <div class="svc" style="left:340px"><div class="photo" style="background:linear-gradient(150deg,#2f4668,#8d9bb0)" role="img" aria-label="Rows of aircraft seats"></div><h3>Aircraft Seats</h3><p>The Company's service team focus is on fast turnaround of seats found in the interior and cargo.</p><span class="btn">Read more</span></div>
  <div class="svc" style="left:620px"><div class="photo" style="background:linear-gradient(150deg,#6f8a5e,#c2c7b3)" role="img" aria-label="Technician testing audio and video units"></div><h3>Remove/Re-Wire Audio/Video</h3><p>The Company's service team focus is on fast turnaround of cabin systems found in the interior and cargo.</p><span class="btn">Read more</span></div>
  <div class="svc" style="left:900px"><div class="photo" style="background:linear-gradient(150deg,#4c6a86,#b7c4cf)" role="img" aria-label="Cargo containers in a hangar"></div><h3>Cargo Equipment</h3><p>The Company's service team focus is on fast turnaround of cargo equipment found in the interior and cargo.</p><span class="btn">Read more</span></div>
</section>

<section class="section products">
  <h2 class="title">STANDARD PRODUCTS</h2>
  <div class="prod" style="left:60px"><div class="photo" style="background:linear-gradient(160deg,#3d3f47,#9a9ea6)" role="img" aria-label="Leather seat covers in a cabin"></div><h4>Leather, E-Leather Covers</h4><span>See more information »</span></div>
  <div class="prod" style="left:343px"><div class="photo" style="background:linear-gradient(160deg,#c9cdd2,#7f8a96)" role="img" aria-label="Cabin curtains"></div><h4>Cabin &amp; Crew Rest Curtains</h4><span>See more information »</span></div>
  <div class="prod" style="left:626px"><div class="photo" style="background:linear-gradient(160deg,#5a4a3e,#b7a592)" role="img" aria-label="Leather cabin accessories"></div><h4>Leather Accoutrements</h4><span>See more information »</span></div>
  <div class="prod" style="left:910px"><div class="photo" style="background:linear-gradient(160deg,#24406b,#7b96bf)" role="img" aria-label="Fabric-covered seats in a cabin"></div><h4>Fabric Covers</h4><span>See more information »</span></div>
</section>

<section class="section partners">
  <h2 class="title">SKYFORGE CUSTOMERS &amp; PARTNERS</h2>
  <svg class="p-arrow" style="left:36px" width="20" height="30"><path d="M15 3 L5 15 L15 27" stroke="#1f5fa6" stroke-width="3" fill="none"/></svg>
  <div class="partner-row">
    <div class="partner">Northwing</div><div class="partner">Aurora Transit Air</div><div class="partner">Meridian Jets</div><div class="partner">Polar Reach Air</div><div class="partner">Tundra Line</div>
  </div>
  <svg class="p-arrow" style="right:36px" width="20" height="30"><path d="M5 3 L15 15 L5 27" stroke="#1f5fa6" stroke-width="3" fill="none"/></svg>
</section>

<footer class="section site-footer">
  <div class="fcol" style="left:40px"><h5>Quick Links</h5><ul><li>Home</li><li>Services</li><li>Plume engineering</li><li>Locations</li><li>People</li><li>Quality</li><li>Sales presentation</li></ul></div>
  <div class="fcol" style="left:260px"><h5>Contact Us</h5><div class="map" role="img" aria-label="Location map"></div></div>
  <div class="fcol" style="left:560px"><h5>Address</h5>
    <div class="addr-line"><svg width="14" height="14"><path d="M7 1a4 4 0 0 1 4 4c0 3-4 8-4 8S3 8 3 5a4 4 0 0 1 4-4z" fill="#c9d3df"/></svg>48 Lumen Avenue, Harbourview, QC</div>
    <div class="addr-line"><svg width="14" height="14"><path d="M3 1h3l1 3-2 1a7 7 0 0 0 4 4l1-2 3 1v3a1 1 0 0 1-1 1A11 11 0 0 1 2 2a1 1 0 0 1 1-1z" fill="#c9d3df"/></svg>(555) 014-2287</div>
    <div class="addr-line"><svg width="14" height="14"><rect x="1" y="3" width="12" height="8" fill="none" stroke="#c9d3df"/><path d="M1 3l6 5 6-5" fill="none" stroke="#c9d3df"/></svg>hello@skyforgenorth.example</div>
  </div>
  <div class="fcol newsletter" style="left:880px"><h5>Newsletter</h5><p>Register your email address to get the latest news from us.</p><div class="field">Email address...</div><span class="btn btn-red">Subscribe</span></div>
  <div class="social"><i></i><i></i><i></i></div>
</footer>
<div class="section footer-bar">© 2016 Skyforge Technics Inc. All rights reserved.</div>

</body>
</html>
```